Coaching business needs flyer for business market

I need a flyer that I can send to HR-managers and business owners to inform them of my coaching services for organisations. We have three services: organisational- and teamcoaching, individual coaching and training programs.
I want the flyer to express calmness, solid and trustworthy coaching. As a person I am open and think out of the box.

In my logo I use a couple of colours (blue, green, orange and grey) that represent the diversity of humans. My company's name is Bramblecrest Engagement & Coaching and tag line is "Awaken your quiet river".

I do not want the design to be too busy but also not too boring. I tried making something myself. Feel free to build on that design. Or feel free to start from scratch.

```html
<!DOCTYPE html>
<html lang="nl">
<head>
<meta charset="utf-8">
<title>Bramblecrest Engagement &amp; Coaching – flyer</title>
<link href="https://fonts.googleapis.com/css2?family=Jost:wght@400;500;600&family=Questrial&display=swap" rel="stylesheet">
<style>
  :root{
    --page-bg:#e9ebee;
    --paper:#ffffff;
    --ink:#2b2623;
    --ink-soft:#4a4440;
    --coral:#ee6b5a;
    --teal:#24969a;
    --mint:#b3e2d6;
    --amber:#f5ad57;
    --sand:#fbe2a2;
    --navy:#2f5e8a;
    --navy-dark:#264f76;
    --sky:#9fd0f5;
    --grey:#6f6f6f;
  }
  *{margin:0;padding:0;box-sizing:border-box}
  html,body{width:1200px;height:1200px;overflow:hidden;background:var(--page-bg)}
  body{font-family:"Questrial",sans-serif;color:var(--ink)}
  .flyer{position:absolute;left:180px;top:6px;width:840px;height:1188px;background:var(--paper);overflow:hidden;box-shadow:0 4px 18px rgba(0,0,0,.12)}
  .abs{position:absolute}

  /* hero */
  .hero{left:0;top:0;width:840px;height:390px;
    background:radial-gradient(ellipse at 48% 0%,#fff6e2 0%,#f1d3a0 22%,#d7ac6c 55%,#b98a4c 100%)}
  .hero-portrait{left:290px;top:50px;width:300px;height:340px;border-radius:150px 150px 0 0;
    background:linear-gradient(180deg,rgba(90,70,55,.35),rgba(150,110,80,.25) 60%,rgba(220,220,230,.35))}
  .tagline{left:51px;top:60px;color:#fff;font-family:"Jost",sans-serif;line-height:1}
  .tagline .t1{display:block;font-size:92px;font-weight:500;letter-spacing:-1px}
  .tagline .t2{display:block;font-size:50px;font-weight:400;margin:8px 0 0 70px}
  .tagline .t3{display:block;font-size:104px;font-weight:500;margin:2px 0 0 10px;letter-spacing:-1px}
  .coach-name{left:564px;top:56px;font-family:"Jost",sans-serif;color:#2a2018;line-height:1}
  .coach-name .first{display:block;font-size:25px;font-weight:500}
  .coach-name .last{display:block;font-size:43px;font-weight:600;margin-top:2px}
  .coach-bio{left:565px;top:141px;width:232px;font-size:11px;line-height:14.1px;color:#2e2620}

  /* service blocks */
  .service h2{font-family:"Jost",sans-serif;font-weight:600;font-size:15px;line-height:16.5px;color:var(--ink)}
  .service h2 em{font-style:normal}
  .rule{height:2px}
  .bullets{list-style:none;font-size:11px;line-height:13.5px;color:var(--ink-soft)}
  .bullets li{position:absolute;padding-left:14px}
  .bullets li::before{content:"";position:absolute;left:0;top:2px;width:8px;height:8px;border:1px solid var(--tick);border-radius:50%}
  .bullets li::after{content:"";position:absolute;left:2.6px;top:3.8px;width:2.5px;height:4px;border:solid var(--tick);border-width:0 1px 1px 0;transform:rotate(45deg)}

  .team em{color:var(--coral)}
  .team .rule{background:var(--coral)}
  .team .bullets{--tick:var(--coral)}
  .individual em{color:var(--teal)}
  .individual .rule{background:var(--mint)}
  .individual .bullets{--tick:var(--teal);opacity:.95}
  .individual .bullets li::before,.individual .bullets li::after{opacity:.6}
  .training em{color:var(--amber)}
  .training .rule{background:var(--sand)}
  .training .bullets{--tick:var(--amber)}

  .photo{background:linear-gradient(135deg,#c9b9a6,#8f7d6d)}
  .photo.dark{background:linear-gradient(160deg,#2a2c3e,#1a1b26 60%,#3a3550)}
  .photo.light{background:linear-gradient(135deg,#e2ddd2,#b8ab99)}

  /* bottom */
  .brand{left:0;top:920px;width:340px;text-align:center;color:var(--grey)}
  .brand-mark{display:block;margin:0 auto 10px;width:82px;height:82px;border:2.5px solid #8a8a8a;border-radius:50%}
  .brand-name{display:block;font-size:40px;line-height:1;color:var(--grey)}
  .brand-sub{display:block;font-size:22px;line-height:1;margin-top:8px;color:var(--grey)}
  .site{left:50px;top:1130px;width:289px;height:27px;border-radius:14px;background:var(--navy);color:#fff;
    font-family:"Jost",sans-serif;font-weight:600;font-size:16px;letter-spacing:4.5px;text-align:center;line-height:27px}
  .methods{left:451px;top:962px;width:380px;color:#fff}
  .methods h3{font-family:"Jost",sans-serif;font-weight:500;font-size:17px;line-height:19.5px;color:var(--sky);text-transform:uppercase}
  .methods ul{list-style:none;margin-top:6px;font-size:12.2px;line-height:17px}
  .methods li{position:relative;padding-left:15px;margin-left:3px}
  .methods li::before{content:"";position:absolute;left:0;top:4px;width:8px;height:8px;border:1px solid #cfe2f2;border-radius:50%}
  .methods b{font-weight:700;font-family:"Jost",sans-serif;font-weight:600}
  .contact{top:1134px;display:flex;align-items:center;gap:8px;font-size:14px;letter-spacing:.6px;color:#333}
  .contact .icon{width:26px;height:26px;border-radius:50%;background:var(--teal);display:flex;align-items:center;justify-content:center}
</style>
</head>
<body>
<main class="flyer">

  <!-- hero -->
  <section class="hero abs" role="img" aria-label="Warm golden light background with a smiling portrait of the coach"></section>
  <div class="hero-portrait abs" role="img" aria-label="Portrait photo of the coach"></div>
  <h1 class="tagline abs"><span class="t1">Awaken</span><span class="t2">your quiet</span><span class="t3">River</span></h1>
  <div class="coach-name abs"><span class="first">Marisol</span><span class="last">Vantveer</span></div>
  <p class="coach-bio abs">is trainer en coach. Ze heeft ruime ervaring met veranderingstrajecten binnen organisaties. Mensen omschrijven haar als ‘betrokken, warm, stevig en kordaat’. Het is haar passie om organisaties, teams en mensen te helpen groeien. Zij helpt weerstand te overwinnen en draagt bij aan groei in zelfvertrouwen. Haar trainingen en coaching zijn erop gericht om snel inzichtelijk te krijgen welke stappen men moet zetten om verder te komen. Ze gelooft de veranderkracht van de mensen waar ze mee werkt. Ze is er om steun en richting te bieden en laat hen zelf aan het roer.</p>

  <!-- team coaching -->
  <section class="service team">
    <h2 class="abs" style="left:50px;top:418px;width:430px">Een organisatie waar medewerkers gemotiveerd zijn, samenwerken, communiceren zonder gedoe door <em>ORGANISATIE- of TEAM coaching:</em></h2>
    <div class="rule abs" style="left:50px;top:473px;width:438px"></div>
    <ul class="bullets">
      <li style="left:51px;top:494px;width:180px">Heb je zorgen voor of na een fusie of verandering?</li>
      <li style="left:247px;top:494px;width:200px">Wens je de cultuur-veranderen of verder ontwikkelen?</li>
      <li style="left:51px;top:534px;width:180px">Wil je missie, visie &amp; strategie ontwikkelen of wijzigen?</li>
      <li style="left:247px;top:534px;width:200px">Beoog je de samenwerking bevorderen of verbeteren?</li>
    </ul>
    <div class="abs" style="left:488px;top:412px;width:20px;height:167px;background:var(--coral)"></div>
    <div class="photo light abs" style="left:508px;top:412px;width:292px;height:167px" role="img" aria-label="Photo of a group workshop in a bright room"></div>
  </section>

  <!-- individual coaching -->
  <section class="service individual">
    <div class="photo abs" style="left:44px;top:579px;width:288px;height:167px" role="img" aria-label="Photo of an individual coaching session"></div>
    <div class="abs" style="left:332px;top:579px;width:21px;height:167px;background:var(--mint)"></div>
    <h2 class="abs" style="left:385px;top:606px;width:420px">Duurzame Inzetbaarheid door <em>INDIVIDUELE Coaching:</em></h2>
    <div class="rule abs" style="left:353px;top:622px;width:445px"></div>
    <ul class="bullets">
      <li style="left:387px;top:641px;width:225px">Wens je medewerkers die hun talent ten volste benutten?</li>
      <li style="left:387px;top:682px;width:225px">Verlang je meer authentieke leiderschap bij je collega’s?</li>
      <li style="left:387px;top:723px;width:225px">Wil je de mensen vooruit helpen in hun loopbaan?</li>
      <li style="left:627px;top:641px;width:175px">Zoek je steun voor medewerkers met burn-out of re-integratie?</li>
      <li style="left:627px;top:695px;width:175px">Heb je hulp nodig bij outplacement trajecten?</li>
    </ul>
  </section>

  <!-- training -->
  <section class="service training">
    <h2 class="abs" style="left:44px;top:776px;width:440px;line-height:19px">Ontwikkeling &amp; Borging van kennis en vakmanschap door <em>LEERGANGEN, TRAININGEN &amp; WORKSHOPS op MAAT:</em></h2>
    <div class="rule abs" style="left:44px;top:811px;width:444px"></div>
    <ul class="bullets">
      <li style="left:44px;top:832px">Leiderschap</li>
      <li style="left:44px;top:856px">Communicatie</li>
      <li style="left:165px;top:832px">Conflicthantering</li>
      <li style="left:165px;top:859px">Leren kijken met ‘systemische blik’ voor professionals</li>
    </ul>
    <div class="abs" style="left:489px;top:761px;width:20px;height:168px;background:var(--sand)"></div>
    <div class="photo dark abs" style="left:509px;top:761px;width:288px;height:168px" role="img" aria-label="Photo of a seminar audience in a dimmed hall"></div>
  </section>

  <!-- bottom band -->
  <svg class="abs" style="left:0;top:880px" width="840" height="250" viewBox="0 0 840 250">
    <defs>
      <linearGradient id="band" x1="0" y1="0" x2="1" y2="1">
        <stop offset="0" stop-color="#3c6a95"/><stop offset="1" stop-color="#2c5882"/>
      </linearGradient>
    </defs>
    <path d="M0 9 H220 C300 9 305 40 330 63" fill="none" stroke="var(--navy)" stroke-width="2.5"/>
    <path d="M323 63 H840 V240 H450 C410 240 395 215 375 160 C358 110 345 80 323 63 Z" fill="url(#band)" role="img" aria-label="Blue-tinted photo of a coaching group"/>
  </svg>

  <div class="brand abs">
    <span class="brand-mark"></span>
    <span class="brand-name">bramblecrest</span>
    <span class="brand-sub">engagement &amp; coaching</span>
  </div>

  <div class="methods abs">
    <h3>Gedegen resultaat en kwaliteit door bewezen ‘best practices’</h3>
    <ul>
      <li>Neuro Linguïstisch Programmeren (NLP)</li>
      <li>Transactionele Analyse</li>
      <li><b>Systemisch Werken:</b> Organisatieopstellingen, Familieopstellingen, Identity oriented Psycho Traumaopstellingen)</li>
      <li>Somatic Experience, Ademwerk en Lichaamswerk</li>
    </ul>
  </div>

  <div class="site abs">www.bramblecrest.nu</div>

  <div class="contact abs" style="left:439px">
    <span class="icon"><svg width="14" height="14" viewBox="0 0 24 24"><path fill="#fff" d="M6.6 10.8a15.1 15.1 0 0 0 6.6 6.6l2.2-2.2a1 1 0 0 1 1-.25 11.4 11.4 0 0 0 3.6.57 1 1 0 0 1 1 1V20a1 1 0 0 1-1 1A17 17 0 0 1 3 4a1 1 0 0 1 1-1h3.5a1 1 0 0 1 1 1c0 1.25.2 2.45.57 3.57a1 1 0 0 1-.25 1z"/></svg></span>
    <span>+31-612480375</span>
  </div>
  <div class="contact abs" style="left:609px">
    <span class="icon"><svg width="14" height="12" viewBox="0 0 24 18"><rect x="1" y="1" width="22" height="16" rx="2" fill="none" stroke="#fff" stroke-width="2"/><path d="M2 2l10 8 10-8" fill="none" stroke="#fff" stroke-width="2"/></svg></span>
    <span>info@bramblecrest.nu</span>
  </div>

</main>
</body>
</html>
```